Pizza Restaurant Needs a New Menu Design

RESTAURANT NAME: The Oven and Barrel House
LOCATION:
- Kyneton, central Victoria Australia
- A small historical country town, with a growing market in visitors from Melbourne coming for food and local activities.
TYPE OF RESTAURANT
Pizza and Pasta restaurant. Modern feel, lots of timber, busy feel.
- Describe the overall restaurant theme/concept
- Ambiance
CLIENTELE:
- Mostly local clientele, but a growing number of tourists also. Local families and young people.
Describe your patrons or your market
OBJECTIVE:
-to give a more modern and professional feel to our menus. They are old and simple and boring.
- hard to read under low light at night.
Why are we updating the old menu?
- What do you like about the old menu that designers should keep or consider when designing
- What do you not like about the old menu?
ADDITIONAL INFORMATION:
www.ovenandbarrelhouse.com.au
https://www.facebook.com/The-Oven-and-Barrel-House-804417362958120/
RESOURCES/ SIZES:
Please find attached all our current menus as requested. With all attachments you will notice 2 of everything. We currently print each menu back to back on white card.
Restaurant 1 and Restaurant 2 - back to back - A3 and then folded
Red Wine and White Wine - back to back A4
Take away 1 and Take away 2 - back to back A4
Dessert - A4 - cut in half
Lunch Menu and Lunch Drink Menu - back to back A4
A3 Takeaway Menu
Thank you :)

```html
<!DOCTYPE html>
<html lang="en">
<head>
<meta charset="utf-8">
<title>The Oven and Barrel House – Menu</title>
<link rel="stylesheet" href="https://fonts.googleapis.com/css2?family=Zilla+Slab:wght@500;700&family=Open+Sans:wght@400;600&display=swap">
<style>
  :root {
    --wine: #a3103c;
    --wine-deep: #8e0c33;
    --panel: rgba(255,255,255,0.16);
    --rule: rgba(255,255,255,0.75);
    --paper: #ffffff;
    --stage: #e4e4e4;
    --ink-light: #ffffff;
  }
  * { box-sizing: border-box; margin: 0; padding: 0; }
  html, body { width: 1107px; height: 1200px; overflow: hidden; background: var(--stage); }
  .spread {
    position: absolute; left: 0; top: 0;
    width: 1300px; height: 920px;
    transform: scale(0.8515); transform-origin: 0 0;
    font-family: "Zilla Slab", Georgia, serif;
    color: var(--ink-light);
  }
  .page { position: absolute; top: 0; width: 648px; height: 920px; background: var(--wine); overflow: hidden; }
  .page--drinks { left: 0; }
  .page--food { left: 652px; }
  .page-gap { position: absolute; left: 648px; top: 0; width: 4px; height: 920px; background: #f3d9e0; }
  .header-art { position: absolute; left: 0; top: 0; width: 648px; height: 210px; }
  .brand {
    position: absolute; left: 224px; top: 64px; width: 200px;
    text-align: center; color: var(--wine-deep);
    font-weight: 700; font-size: 24px; line-height: 1.05; text-transform: uppercase;
  }
  .abs { position: absolute; }
  .drinks-bar {
    left: 0; top: 205px; width: 438px; height: 31px; background: var(--paper);
    color: var(--wine-deep); font-weight: 700; font-size: 18px; padding: 4px 0 0 20px;
  }
  .tab {
    background: var(--paper); color: var(--wine-deep); font-weight: 700;
    font-size: 17px; height: 21px; padding: 0 0 0 6px; line-height: 21px;
    border-radius: 0 0 8px 0;
  }
  .soft-panel { left: 20px; top: 245px; width: 272px; height: 613px; background: var(--panel); border-radius: 8px; }
  .rule { height: 2px; background: var(--rule); }
  .line { font-size: 11.5px; font-weight: 700; white-space: nowrap; }
  .line .note { font-family: "Open Sans", Arial, sans-serif; font-weight: 400; font-size: 10.5px; }
  .price { font-size: 13px; font-weight: 700; text-align: right; }
  .beer { font-size: 13px; font-weight: 700; white-space: nowrap; }
  .wine-ask { font-size: 17px; font-weight: 700; }
  .small-ask { font-size: 10px; font-weight: 700; }
  .menu-title { left: 38px; top: 150px; font-size: 40px; font-weight: 700; }
  .section-title { left: 38px; top: 216px; font-size: 26px; font-weight: 700; }
  .starter { left: 70px; width: 480px; text-align: center; }
  .starter h3 { font-size: 16px; font-weight: 700; line-height: 17px; }
  .starter p { font-family: "Open Sans", Arial, sans-serif; font-size: 10.5px; line-height: 13px; }
  .starter strong { font-family: "Zilla Slab", Georgia, serif; font-weight: 700; }
  .starter-price { right: 30px; font-size: 18px; font-weight: 700; line-height: 18px; }
  .promise { left: 30px; width: 590px; top: 822px; text-align: center; font-size: 13px; font-weight: 700; line-height: 16px; }
  .notice {
    left: 65px; top: 884px; width: 514px; height: 40px; background: var(--paper);
    border-radius: 20px 20px 0 0; color: var(--wine-deep);
    font-size: 11px; font-weight: 700; text-align: center; padding-top: 11px;
  }
</style>
</head>
<body>
<main class="spread">

  <section class="page page--drinks">
    <svg class="header-art" viewBox="0 0 648 210" role="img" aria-label="Line drawings of food, coffee cups and drinks across the top band">
      <path d="M0 40 C150 40 200 200 325 200 C450 200 500 40 648 30 L648 0 L0 0 Z" fill="var(--paper)"/>
      <circle cx="325" cy="115" r="78" fill="#f7e6eb"/>
    </svg>
    <div class="brand">The Oven and Barrel House</div>

    <div class="abs drinks-bar">Drinks (BYO wine only – corkage $5.00 per bottle)</div>

    <div class="abs soft-panel"></div>
    <div class="abs tab" style="left:20px;top:246px;width:150px;">Non alcoholic</div>

    <div class="abs line" style="left:24px;top:279px;">Juice <span class="note">– orange, apple</span></div>
    <div class="abs line" style="left:24px;top:295px;">Mineral water <span class="note">– natural</span></div>
    <div class="abs line" style="left:24px;top:311px;">Sparkling Apple</div>
    <div class="abs line" style="left:24px;top:327px;">Bottled still water <span class="note">– 600ml</span></div>
    <div class="abs line" style="left:24px;top:343px;">Dry ginger, Tonic, Soda</div>
    <div class="abs line" style="left:24px;top:359px;">Chinotto <span class="note">– Italian cola</span></div>
    <div class="abs price" style="left:200px;top:357px;width:52px;">$3.50</div>
    <div class="abs rule" style="left:20px;top:389px;width:266px;"></div>

    <div class="abs line" style="left:24px;top:410px;">Cola, Diet Cola, Cola Zero, Lemon Squash, Lemonade</div>
    <div class="abs line" style="left:24px;top:430px;">Orange, Raspberry – 375ml can -</div>
    <div class="abs price" style="left:230px;top:429px;width:52px;">$2.50</div>
    <div class="abs line" style="left:24px;top:450px;">Ginger Beer - 300ml glass bottle</div>
    <div class="abs price" style="left:230px;top:449px;width:52px;">$4.50</div>
    <div class="abs line" style="left:24px;top:470px;">Cola - 300ml glass bottle</div>
    <div class="abs price" style="left:230px;top:469px;width:52px;">$4.50</div>
    <div class="abs line" style="left:26px;top:490px;">Jug -</div>
    <div class="abs price" style="left:230px;top:489px;width:52px;">$8.00</div>
    <div class="abs rule" style="left:20px;top:507px;width:266px;"></div>

    <div class="abs line" style="left:24px;top:519px;">Milkshake – Chocolate, Strawberry, Caramel</div>
    <div class="abs line" style="left:24px;top:532px;">Blue Heaven, Lime or Vanilla Malt</div>
    <div class="abs price" style="left:230px;top:531px;width:52px;">$6.00</div>
    <div class="abs line" style="left:24px;top:559px;">Spiders</div>
    <div class="abs price" style="left:230px;top:558px;width:52px;">$5.00</div>
    <div class="abs line" style="left:24px;top:573px;">Iced Chocolate / Coffee</div>
    <div class="abs price" style="left:230px;top:572px;width:52px;">$5.00</div>
    <div class="abs rule" style="left:20px;top:614px;width:266px;"></div>

    <div class="abs line" style="left:24px;top:633px;">Cappucino</div>
    <div class="abs line" style="left:24px;top:653px;">Flat White</div>
    <div class="abs line" style="left:24px;top:673px;">Café latte</div>
    <div class="abs line" style="left:24px;top:693px;">Short Black</div>
    <div class="abs line" style="left:24px;top:713px;">Long Black</div>
    <div class="abs line" style="left:24px;top:733px;">Long macchiato</div>
    <div class="abs line" style="left:24px;top:753px;">Short macchiato</div>
    <div class="abs line" style="left:24px;top:773px;">Chai Latte</div>
    <div class="abs line" style="left:24px;top:792px;">Tea – variety, please ask</div>
    <div class="abs price" style="left:230px;top:791px;width:52px;">$3.50</div>
    <div class="abs line" style="left:24px;top:812px;">$4.00 mug</div>
    <div class="abs line" style="left:24px;top:832px;">Hot Chocolate</div>
    <div class="abs price" style="left:230px;top:831px;width:52px;">$4.00</div>

    <div class="abs small-ask" style="left:24px;top:862px;">Soy Milk and Decaf coffee available</div>
    <div class="abs wine-ask" style="left:24px;top:876px;">Please ask staff for our Wine List</div>

    <div class="abs tab" style="left:307px;top:269px;width:151px;">Beer</div>
    <div class="abs beer" style="left:307px;top:298px;">Marisol Lager</div>
    <div class="abs price" style="left:565px;top:298px;width:60px;">$7.00</div>
    <div class="abs beer" style="left:307px;top:323px;">Kingsfield Lager</div>
    <div class="abs price" style="left:565px;top:323px;width:60px;">$7.00</div>
    <div class="abs beer" style="left:307px;top:347px;">Fernbrook Pilsner (Ashvale)</div>
    <div class="abs price" style="left:565px;top:347px;width:60px;">$7.00</div>
    <div class="abs beer" style="left:307px;top:372px;">Fernbrook Hilltop Ale (Ashvale)</div>
    <div class="abs price" style="left:565px;top:372px;width:60px;">$7.00</div>
    <div class="abs beer" style="left:307px;top:396px;">Lookout American Pale Ale (Millbrook)</div>
    <div class="abs price" style="left:565px;top:396px;width:60px;">$7.00</div>
    <div class="abs beer" style="left:307px;top:421px;">Tanner's Pale Ale</div>
    <div class="abs price" style="left:565px;top:421px;width:60px;">$7.00</div>
    <div class="abs beer" style="left:307px;top:446px;">Riverbend Bitter</div>
    <div class="abs price" style="left:565px;top:446px;width:60px;">$5.50</div>
    <div class="abs beer" style="left:307px;top:470px;">Stonebridge Draught</div>
    <div class="abs price" style="left:565px;top:470px;width:60px;">$5.50</div>
    <div class="abs beer" style="left:307px;top:495px;">Sunny Blonde</div>
    <div class="abs price" style="left:565px;top:495px;width:60px;">$6.00</div>
    <div class="abs beer" style="left:307px;top:519px;">Vespera (Italy)</div>
    <div class="abs price" style="left:565px;top:519px;width:60px;">$7.00</div>
    <div class="abs beer" style="left:307px;top:544px;">Old Mill Light</div>
    <div class="abs price" style="left:565px;top:544px;width:60px;">$5.00</div>
    <div class="abs beer" style="left:307px;top:569px;">Glacier Premium Light</div>
    <div class="abs price" style="left:565px;top:569px;width:60px;">$5.00</div>

    <div class="abs tab" style="left:309px;top:652px;width:162px;">Mixed Drinks</div>
    <div class="abs beer" style="left:309px;top:698px;">Red Oak Bourbon – glass bottle</div>
    <div class="abs price" style="left:560px;top:698px;width:60px;">$8.00</div>
    <div class="abs beer" style="left:309px;top:717px;">Copper Still Whiskey – glass bottle</div>
    <div class="abs price" style="left:560px;top:717px;width:60px;">$8.00</div>
    <div class="abs beer" style="left:309px;top:754px;">Scotch, Canefield Rum,</div>
    <div class="abs beer" style="left:309px;top:773px;">Bourbon, Gin, Vodka, Brandy</div>
    <div class="abs price" style="left:558px;top:773px;width:60px;">$7.00</div>
    <div class="abs beer" style="left:309px;top:810px;">Lemon, Lime &amp; Bitters</div>
    <div class="abs price" style="left:558px;top:810px;width:60px;">$6.00</div>
    <div class="abs beer" style="left:309px;top:829px;">Frostberry – Wild Berries</div>
    <div class="abs price" style="left:558px;top:829px;width:60px;">$6.00</div>
    <div class="abs beer" style="left:309px;top:848px;">Orchard Lane Cider – Apple or Pear</div>
    <div class="abs price" style="left:558px;top:848px;width:60px;">$7.00</div>
    <div class="abs beer" style="left:309px;top:885px;">Lambrusco – chilled sweet red</div>
    <div class="abs price" style="left:500px;top:885px;width:118px;">glass $6.00</div>
    <div class="abs price" style="left:500px;top:903px;width:118px;">bottle $18.00</div>
  </section>

  <div class="page-gap"></div>

  <section class="page page--food">
    <svg class="header-art" viewBox="0 0 648 210" role="img" aria-label="Line drawings of food, coffee cups and desserts across the top band">
      <path d="M0 40 C150 40 200 200 325 200 C450 200 500 40 648 30 L648 0 L0 0 Z" fill="var(--paper)"/>
      <circle cx="323" cy="115" r="78" fill="#f7e6eb"/>
    </svg>
    <div class="brand" style="left:222px;">The Oven and Barrel House</div>

    <h1 class="abs menu-title">Menu</h1>
    <h2 class="abs section-title">Starters</h2>

    <div class="abs starter" style="top:264px;"><h3>Garlic Bread</h3><p>Serves 2</p></div>
    <div class="abs starter-price" style="top:277px;">$4.00</div>
    <div class="abs starter" style="top:299px;"><h3>Foccacia</h3><p>Garlic &amp; herb pizza (add tasty mozzarella cheese .60¢)</p></div>
    <div class="abs starter-price" style="top:312px;">$7.00</div>
    <div class="abs starter" style="top:334px;"><h3>House Dips</h3><p>Selection of dips served with a garlic and herb foccacia</p></div>
    <div class="abs starter-price" style="top:347px;">$15.00</div>
    <div class="abs starter" style="top:370px;"><h3>Greek Style Salad</h3><p>lettuce, cherry tomato, fetta, red onion, capsicum, olives and house made dressing<br>(optional house made balsamic dressing)</p></div>
    <div class="abs starter-price" style="top:386px;">$12.00</div>
    <div class="abs starter" style="top:423px;"><h3>Caesar Salad</h3><p>lettuce, croutons, bacon, parmesan with Caesar dressing (anchovies on request)</p></div>
    <div class="abs starter-price" style="top:436px;">$12.00</div>
    <div class="abs starter" style="top:458px;"><h3>Chicken Caesar</h3><p>chicken, lettuce, croutons, bacon, parmesan &amp; Caesar dressing (anchovies on request)</p></div>
    <div class="abs starter-price" style="top:470px;">$14.00</div>
    <div class="abs starter" style="top:492px;"><h3>King Prawn Salad</h3><p>prawns, cherry tomato, avocado, red onion, capsicum, lettuce &amp; Caesar dressing</p></div>
    <div class="abs starter-price" style="top:502px;">$16.00</div>
    <div class="abs starter" style="top:527px;"><h3>Angus Salad</h3><p>spinach, pumpkin, semi-dried tomato, pinenuts and fetta tossed in balsamic</p></div>
    <div class="abs starter-price" style="top:538px;">$12.00</div>
    <div class="abs starter" style="top:558px;"><h3>Calamari</h3><p>tender crumbed calamari rings with tartare &amp; sweet chilli sauce<br>– <strong>Main Calamari</strong> served with a side salad</p></div>
    <div class="abs starter-price" style="top:568px;">$14.00</div>
    <div class="abs starter-price" style="top:584px;">$17.00</div>
    <div class="abs starter" style="top:604px;"><h3>Wedges</h3><p>crispy potato wedges served with sweet chilli and sour cream<br>– <strong>Main Wedges</strong> served with a side salad</p></div>
    <div class="abs starter-price" style="top:616px;">$14.00</div>
    <div class="abs starter-price" style="top:633px;">$17.00</div>
    <div class="abs starter" style="top:653px;"><h3>Lamb ribs</h3><p>Marinated lamb ribs oven roasted, served medium rare<br>– <strong>Main Ribs</strong> served with a side salad</p></div>
    <div class="abs starter-price" style="top:663px;">$15.00</div>
    <div class="abs starter-price" style="top:681px;">$19.00</div>
    <div class="abs starter" style="top:700px;"><h3>Side Salad</h3><p>mixed lettuce, tomato, red onion, olives, capsicum and fetta with house dressing</p></div>
    <div class="abs starter-price" style="top:710px;">$6.00</div>
    <div class="abs starter" style="top:736px;"><h3>Side Wedges</h3><p>crispy potato wedges</p></div>
    <div class="abs starter-price" style="top:745px;">$6.00</div>

    <p class="abs promise">All pizzas, sauces, lasagnes etc are made on our premises, using traditional Italian recipes<br>and the freshest possible ingredients.</p>
    <p class="abs notice">* We cannot guarantee gluten free as flour and cheese products are made in our kitchen.</p>
  </section>

</main>
</body>
</html>
```